Natural Stone Company Redesign

Looking for a fresh, creative, website design. We service Luxury Residential projects in US and Internationally. We would like to see a design that communicates a passion for creative challenging design that is merged with natural stone projects. Our new company Logo is "Quarry & Quill"

We like to emphasis from concept to completion, for example, photos of blueprints and/or sketches of a project, then a completion photo of same project.

some websites we like are:
http://www.brelmofask.com/
http://tovanquistdesign.com/

We would like to highlight our services of "concept to completion" scenario. Blueprints/sketches to finished products.
Page needed:
Home
About Us
Projects
Contact Us

Target Market(s)

Developers, architects, designers

Industry/Entity Type

It Company

Number of Pages Required

4 page

Font styles to use
Sans Serif

Requirements
Must have
• "Quarry & Quill"
• New, innovative, look.
• Something to grab the attention, and make them think
Nice to have
• Motion on the homepage
• Roll over the finished project photo, and have the name of the stone pop up

```html
<!DOCTYPE html>
<html lang="en">
<head>
<meta charset="utf-8">
<title>Contact us – Quarry &amp; Quill</title>
<link rel="stylesheet" href="https://fonts.googleapis.com/css2?family=Poppins:wght@200;300;400;500;600&family=Montserrat:wght@600;700&family=Roboto:wght@400;500&display=swap">
<style>
  :root {
    --orange: #ff8535;
    --ink: #1f1f24;
    --muted: #9a9a9a;
    --rule: #e2e2e2;
    --footer-bg: #21232f;
    --footer-text: #a6a9b6;
    --footer-rule: #363949;
    --white: #ffffff;
  }
  * { margin: 0; padding: 0; box-sizing: border-box; }
  html, body { width: 1046px; height: 1200px; overflow: hidden; background: var(--white); }
  body { position: relative; font-family: "Poppins", sans-serif; color: var(--ink); }
  .abs { position: absolute; }

  /* Header */
  .site-header { position: absolute; left: 0; top: 0; width: 1046px; height: 68px; background: var(--white); }
  .brand { position: absolute; left: 77px; top: 20px; font-size: 19px; font-weight: 300; letter-spacing: 0.2px; }
  .menu-toggle { position: absolute; left: 952px; top: 26px; width: 18px; height: 16px; }
  .menu-toggle span { position: absolute; left: 0; width: 18px; height: 1.5px; background: var(--ink); }

  /* Hero */
  .page-hero { position: absolute; left: 0; top: 68px; width: 1046px; height: 170px;
    background: linear-gradient(180deg, #6f747f 0%, #8a8a88 45%, #6b6257 75%, #3d3a38 100%); }
  .page-hero h1 { position: absolute; left: 0; width: 100%; top: 56px; text-align: center;
    color: var(--white); font-weight: 300; font-size: 32px; letter-spacing: 0.5px; }
  .breadcrumb { position: absolute; left: 0; width: 100%; top: 106px; text-align: center;
    color: var(--white); font-family: "Roboto", sans-serif; font-size: 11px; font-weight: 500; }
  .breadcrumb .sep { margin: 0 9px; }

  /* Contact form */
  .contact-form { position: absolute; left: 143px; top: 304px; width: 450px; height: 550px; background: var(--orange); }
  .form-title { position: absolute; left: 0; width: 100%; top: 36px; text-align: center;
    font-family: "Montserrat", sans-serif; font-weight: 700; font-size: 15px; color: var(--white); letter-spacing: 0.6px; }
  .field-label { position: absolute; left: 29px; font-family: "Roboto", sans-serif; font-size: 10px;
    font-weight: 500; color: rgba(255,255,255,0.72); letter-spacing: 0.3px; }
  .field-line { position: absolute; left: 29px; width: 392px; height: 1.5px; background: var(--white); }
  .field-value { position: absolute; left: 29px; top: 127px; font-size: 19px; font-weight: 400; color: var(--white); }
  .field-value .caret { opacity: 0.6; font-weight: 200; margin-left: 2px; }
  .send-btn { position: absolute; left: 211px; top: 474px; width: 209px; height: 42px; background: #000;
    color: var(--white); font-family: "Roboto", sans-serif; font-size: 10px; font-weight: 500; }
  .send-btn .label { position: absolute; left: 0; width: 209px; top: 15px; text-align: center; }
  .send-btn svg { position: absolute; left: 187px; top: 16px; }

  /* Contact information */
  .info-index { position: absolute; left: 654px; top: 292px; font-size: 38px; font-weight: 200; }
  .info-heading-bar { position: absolute; left: 655px; top: 354px; width: 2px; height: 61px; background: var(--orange); }
  .info-heading { position: absolute; left: 678px; top: 359px; font-size: 24px; font-weight: 300; line-height: 31px; }
  .info-label { position: absolute; left: 655px; font-family: "Roboto", sans-serif; font-size: 11px;
    font-weight: 500; color: var(--muted); letter-spacing: 0.2px; }
  .info-bar { position: absolute; left: 655px; width: 1.5px; height: 38px; background: var(--rule); }
  .info-value { position: absolute; left: 686px; font-size: 14px; font-weight: 300; }

  /* Footer */
  .site-footer { position: absolute; left: 0; top: 932px; width: 1046px; height: 268px; background: var(--footer-bg); }
  .footer-heading { position: absolute; top: 60px; font-size: 15px; font-weight: 400; color: var(--white); }
  .footer-underline { position: absolute; top: 86px; width: 20px; height: 2px; background: var(--orange); }
  .footer-item { position: absolute; font-family: "Roboto", sans-serif; font-size: 11px; color: var(--footer-text); }
  .footer-item svg { position: absolute; left: -15px; top: 2px; }
  .newsletter-input { position: absolute; left: 692px; top: 108px; font-size: 12.5px; font-weight: 300; color: var(--footer-text); }
  .newsletter-line { position: absolute; left: 692px; top: 134px; width: 276px; height: 1px; background: #d8d8de; }
  .newsletter-btn { position: absolute; left: 693px; top: 148px; width: 37px; height: 24px; border-radius: 12px; background: var(--orange); }
  .newsletter-btn svg { position: absolute; left: 13px; top: 6px; }
  .footer-rule { position: absolute; left: 78px; top: 221px; width: 890px; height: 1px; background: var(--footer-rule); }
  .copyright { position: absolute; left: 78px; top: 237px; font-family: "Roboto", sans-serif; font-size: 11px; color: var(--white); }
  .to-top { position: absolute; left: 990px; top: 203px; width: 36px; height: 36px; border-radius: 50%; background: #383b48; }
  .to-top svg { position: absolute; left: 13px; top: 11px; }
</style>
</head>
<body>

<header class="site-header">
  <div class="brand">Quarry &amp; Quill</div>
  <div class="menu-toggle" aria-label="Menu">
    <span style="top:0"></span><span style="top:7px"></span><span style="top:14px"></span>
  </div>
</header>

<section class="page-hero" role="img" aria-label="Photograph of a modern stone-clad house at dusk">
  <h1>Contact us</h1>
  <div class="breadcrumb">HOME<span class="sep">&gt;</span>CONTACT US</div>
</section>

<form class="contact-form">
  <div class="form-title">GET IN TOUCH</div>

  <div class="field-label" style="top:106px">FULL NAME</div>
  <div class="field-value">John Georg<span class="caret">|</span></div>
  <div class="field-line" style="top:166px"></div>

  <div class="field-label" style="top:200px">EMAIL ADDRESS</div>
  <div class="field-line" style="top:259px"></div>

  <div class="field-label" style="top:294px">MESSAGE</div>
  <div class="field-line" style="top:438px"></div>

  <div class="send-btn">
    <span class="label">SEND</span>
    <svg width="11" height="10" viewBox="0 0 11 10" fill="none" stroke="#fff" stroke-width="1.2">
      <path d="M0 5h10M6 1l4 4-4 4"/>
    </svg>
  </div>
</form>

<div class="info-index">01</div>
<div class="info-heading-bar"></div>
<div class="info-heading">Contact<br>Information</div>

<div class="info-label" style="top:477px">EMAIL ADDRESS</div>
<div class="info-bar" style="top:504px"></div>
<div class="info-value" style="top:514px">info@emailaddress.com</div>

<div class="info-label" style="top:592px">PHONE NUMBER</div>
<div class="info-bar" style="top:619px"></div>
<div class="info-value" style="top:628px">123 - 456 - 7890</div>

<div class="info-label" style="top:709px">LOCATION</div>
<div class="info-bar" style="top:736px"></div>
<div class="info-value" style="top:746px">Some address line goes here...</div>

<footer class="site-footer">
  <div class="footer-heading" style="left:78px">Location &amp; Contact Info</div>
  <div class="footer-underline" style="left:78px"></div>
  <div class="footer-item" style="left:92px;top:104px">
    <svg width="8" height="10" viewBox="0 0 8 10"><path d="M4 0a4 4 0 0 0-4 4c0 3 4 6 4 6s4-3 4-6a4 4 0 0 0-4-4z" fill="#ff8535"/><circle cx="4" cy="4" r="1.4" fill="#21232f"/></svg>
    Some address line goes here, City name, Country name.</div>
  <div class="footer-item" style="left:92px;top:129px">
    <svg width="9" height="9" viewBox="0 0 9 9"><path d="M2 0l1.6 2.2-1 1.1a6 6 0 0 0 3 3l1.1-1L9 7l-1 2C4 9 0 5 0 1z" fill="#ff8535"/></svg>
    123 546 7890</div>
  <div class="footer-item" style="left:92px;top:154px">
    <svg width="9" height="7" viewBox="0 0 9 7"><rect width="9" height="7" fill="#ff8535"/><path d="M0 0l4.5 3.5L9 0" stroke="#21232f" fill="none" stroke-width="0.9"/></svg>
    info@email.com</div>

  <div class="footer-heading" style="left:462px">Useful Links</div>
  <div class="footer-underline" style="left:463px"></div>
  <div class="footer-item" style="left:463px;top:104px">›&nbsp; Home</div>
  <div class="footer-item" style="left:463px;top:123px">›&nbsp; Privacy Policy</div>
  <div class="footer-item" style="left:463px;top:142px">›&nbsp; Terms &amp; Conditions</div>

  <div class="footer-heading" style="left:692px">Newsletter</div>
  <div class="footer-underline" style="left:692px"></div>
  <div class="newsletter-input">Enter your email address...</div>
  <div class="newsletter-line"></div>
  <div class="newsletter-btn">
    <svg width="11" height="11" viewBox="0 0 11 11"><path d="M11 0L0 4.5l4 1.5 1.5 4z" fill="#fff"/></svg>
  </div>

  <div class="footer-rule"></div>
  <div class="copyright">© 2017, All Rights Reserved.</div>
  <div class="to-top" aria-label="Back to top">
    <svg width="10" height="13" viewBox="0 0 10 13" fill="none" stroke="#fff" stroke-width="1.1"><path d="M5 13V1M1 5l4-4 4 4"/></svg>
  </div>
</footer>

</body>
</html>
```